BWK Business Card

A double sided business card based on your "Brightwater Keystone Ltd" Logo. To use the "BWK" logo on 1 side and the full company logo on the reverse.

Detials to be included:

Name: Tom Pellow
Postion: Consultant Orthotist & Expert Witness
T: +44 (0) 7958 302146
F: +44 (0) 7465 8810

```html
<!DOCTYPE html>
<html lang="en">
<head>
<meta charset="utf-8">
<title>BWK Business Card</title>
<link rel="stylesheet" href="https://fonts.googleapis.com/css2?family=EB+Garamond:wght@400;600;700&display=swap">
<style>
  :root {
    --navy: #0f3c74;
    --grey: #9a9a9a;
    --grey-light: #c9c9c9;
    --ink: #2b2b2b;
    --paper: #ffffff;
    --backdrop: #e6e6ea;
  }
  * { box-sizing: border-box; margin: 0; padding: 0; }
  html, body { width: 1200px; height: 987px; overflow: hidden; }
  body {
    background: var(--backdrop);
    font-family: "EB Garamond", Georgia, serif;
    color: var(--ink);
    position: relative;
  }
  .card {
    position: absolute;
    left: 220px;
    width: 760px;
    height: 434px;
    background: var(--paper);
    border-radius: 24px;
    box-shadow: 0 6px 18px rgba(0,0,0,0.14);
    overflow: hidden;
  }
  .card--brand { top: 36px; }
  .card--contact { top: 517px; }

  .mark {
    position: absolute;
    display: flex;
    align-items: center;
    gap: 14px;
    color: var(--navy);
    font-weight: 600;
    letter-spacing: 4px;
  }
  .mark__square {
    width: 22px; height: 22px;
    background: var(--grey);
  }
  .divider {
    position: absolute;
    width: 2px;
    background: var(--grey-light);
  }

  /* brand side */
  .card--brand .mark { left: 78px; top: 178px; font-size: 64px; }
  .card--brand .divider { left: 336px; top: 120px; height: 194px; }
  .company {
    position: absolute;
    left: 364px; top: 142px;
    color: var(--navy);
  }
  .company__name {
    font-size: 46px;
    font-weight: 600;
    line-height: 0.98;
    text-transform: uppercase;
    letter-spacing: 1px;
  }
  .company__rule {
    height: 2px; background: var(--grey); margin: 10px 0 6px; width: 340px;
  }
  .company__tagline {
    font-size: 16px;
    font-variant: small-caps;
    letter-spacing: 1px;
    color: var(--ink);
    font-weight: 600;
  }

  /* contact side */
  .swoosh { position: absolute; left: 0; top: 0; }
  .card--contact .mark { left: 70px; top: 60px; font-size: 70px; }
  .card--contact .divider { left: 344px; top: 50px; height: 200px; }
  .details {
    position: absolute;
    left: 372px; top: 56px;
  }
  .details__name {
    color: var(--navy);
    font-size: 30px;
    font-weight: 700;
    line-height: 1.1;
  }
  .details__role {
    color: var(--grey);
    font-size: 20px;
    margin-bottom: 10px;
  }
  .details__address { font-size: 21px; line-height: 1.2; margin-bottom: 8px; }
  .contact-line {
    display: flex; align-items: center; gap: 10px;
    font-size: 21px; line-height: 1.35;
  }
  .contact-line svg { width: 18px; height: 18px; flex: none; }
</style>
</head>
<body>

<section class="card card--brand" aria-label="Business card, company side">
  <div class="mark"><span class="mark__square"></span>BWK</div>
  <div class="divider"></div>
  <div class="company">
    <div class="company__name">Brightwater<br>Keystone Ltd</div>
    <div class="company__rule"></div>
    <div class="company__tagline">Excellence in Medical Legal Reporting</div>
  </div>
</section>

<section class="card card--contact" aria-label="Business card, contact side">
  <svg class="swoosh" width="760" height="434" viewBox="0 0 760 434">
    <path d="M0 160 C 150 220, 300 330, 420 434 L0 434 Z" fill="var(--grey-light)"/>
    <path d="M0 150 C 160 210, 310 330, 440 434 L405 434 C 290 340, 150 235, 0 182 Z" fill="var(--navy)"/>
    <path d="M0 215 C 140 270, 260 360, 340 434 L0 434 Z" fill="var(--grey)"/>
    <path d="M380 434 C 420 420, 470 420, 520 434 Z" fill="var(--navy)"/>
  </svg>
  <div class="mark"><span class="mark__square"></span>BWK</div>
  <div class="divider"></div>
  <div class="details">
    <div class="details__name">Tom Pellow</div>
    <div class="details__role">Consultant Orthotist &amp; Expert Witness</div>
    <div class="details__address">18 Harlow Lane Kingston<br>Surrey, KT3 4PX</div>
    <div class="contact-line">
      <svg viewBox="0 0 20 20" aria-hidden="true"><circle cx="10" cy="10" r="10" fill="var(--navy)"/><path d="M6 5 L8 5 L9 8 L8 9 C9 11 10 12 11 12 L12 11 L15 12 L15 14 C10 15 5 10 6 5Z" fill="#fff"/></svg>
      <span>+44 (0) 7958 302146</span>
    </div>
    <div class="contact-line">
      <svg viewBox="0 0 20 20" aria-hidden="true"><rect x="2" y="8" width="16" height="9" rx="2" fill="var(--navy)"/><rect x="5" y="3" width="10" height="6" fill="var(--navy)"/><rect x="6" y="11" width="8" height="2" fill="#fff"/></svg>
      <span>+44 (0) 7465 8810</span>
    </div>
    <div class="contact-line">
      <svg viewBox="0 0 20 20" aria-hidden="true"><rect x="1" y="4" width="18" height="12" rx="2" fill="var(--navy)"/><path d="M2 5 L10 11 L18 5" stroke="#fff" stroke-width="1.6" fill="none"/></svg>
      <span>tom@brightwaterkeystone.co.uk</span>
    </div>
  </div>
</section>

</body>
</html>
```